Life Coach for Lawyers Business Card Design

Elegant, original, business card design for life coaching service for associate attorneys who work in big law and struggle with stress, overwhelm, and time management. Double sided design.

Target Market(s)

Women associate attorneys who work in big law and struggle with stress, overwhelm, and time management.

Industry/Entity Type

Life Coaching

Contact Information for Business Card

Marlene Quorthby
Life Coach
519.607.4431
brightcounselpath.net
marlene@brightcounselpath.net
@brightcounselpath (Instagram)

Font styles to use
Other font styles liked:
• Silver South font duo. See uploaded files.

Requirements
Must have
• Icons for phone, website, email, and Instagram instead of words. Specific colors used in my logo (171B2B, 421121, FFFFFF)
Nice to have
• Foil. Embossed. Feminine design.
Should not have
• Any colors other than those used in logo. See uploaded files.

```html
<!DOCTYPE html>
<html lang="en">
<head>
<meta charset="UTF-8">
<title>Bright Counsel Path – Business Card</title>
<link href="https://fonts.googleapis.com/css2?family=Montserrat:wght@400;700&family=Playfair+Display:wght@600&display=swap" rel="stylesheet">
<style>
  :root {
    --navy: #171B2B;
    --wine: #421121;
    --white: #FFFFFF;
    --band: #6C6977;
    --backdrop: #E9E8EC;
    --rule: #55535c;
  }
  * { box-sizing: border-box; margin: 0; padding: 0; }
  html, body { width: 1200px; height: 900px; overflow: hidden; }
  body {
    background: var(--backdrop);
    display: flex;
    align-items: center;
    justify-content: center;
    gap: 80px;
    font-family: "Montserrat", Arial, sans-serif;
    color: var(--navy);
  }
  .card {
    position: relative;
    width: 360px;
    height: 600px;
    background: var(--white);
    border-radius: 30px;
    overflow: hidden;
    box-shadow: 0 10px 30px rgba(23, 27, 43, 0.18);
  }
  .card--front {
    display: flex;
    flex-direction: column;
    align-items: center;
    padding: 56px 30px 40px;
    text-align: center;
  }
  .brand-name {
    font-family: "Playfair Display", Georgia, serif;
    font-weight: 600;
    color: var(--wine);
    letter-spacing: 0.5px;
    line-height: 1.15;
  }
  .card--front .brand-name { font-size: 24px; white-space: nowrap; }
  .holder-name {
    margin-top: 12px;
    font-size: 21px;
    font-weight: 700;
  }
  .holder-role {
    font-size: 13px;
    font-weight: 400;
    margin-top: 2px;
  }
  .rule {
    width: 210px;
    height: 1px;
    background: var(--rule);
    margin: 16px 0;
  }
  .contact-item {
    display: flex;
    flex-direction: column;
    align-items: center;
    gap: 10px;
  }
  .contact-icon { width: 26px; height: 26px; }
  .contact-icon--solid { fill: var(--wine); }
  .contact-icon--line {
    fill: none;
    stroke: var(--wine);
    stroke-width: 1.8;
    stroke-linejoin: round;
    stroke-linecap: round;
  }
  .contact-text { font-size: 16px; font-weight: 700; }
  .contact-text--small { font-size: 14px; }
  .card--back .bands { position: absolute; inset: 0; width: 100%; height: 100%; }
  .band { fill: var(--band); }
  .card--back .brand-name {
    position: absolute;
    top: 50%;
    left: 50%;
    transform: translate(-50%, -50%);
    font-size: 30px;
    text-align: center;
    width: 230px;
  }
</style>
</head>
<body>

  <section class="card card--front">
    <div class="brand-name">Bright Counsel Path</div>
    <div class="holder-name">Marlene Quorthby</div>
    <div class="holder-role">Life Coach</div>
    <div class="rule"></div>

    <div class="contact-item">
      <svg class="contact-icon contact-icon--solid" viewBox="0 0 24 24" aria-hidden="true">
        <path d="M6.6 10.8a15.1 15.1 0 0 0 6.6 6.6l2.2-2.2a1 1 0 0 1 1-.25 11.4 11.4 0 0 0 3.6.57 1 1 0 0 1 1 1V20a1 1 0 0 1-1 1A17 17 0 0 1 3 4a1 1 0 0 1 1-1h3.5a1 1 0 0 1 1 1c0 1.25.2 2.45.57 3.57a1 1 0 0 1-.25 1z"/>
      </svg>
      <div class="contact-text">519.607.4431</div>
    </div>
    <div class="rule"></div>

    <div class="contact-item">
      <svg class="contact-icon contact-icon--line" viewBox="0 0 24 24" aria-hidden="true">
        <rect x="2.5" y="5" width="19" height="14" rx="1"/>
        <path d="M3.5 6.5 12 13l8.5-6.5"/>
      </svg>
      <div class="contact-text contact-text--small">brightcounselpath.net</div>
    </div>
    <div class="rule"></div>

    <div class="contact-item">
      <svg class="contact-icon contact-icon--line" viewBox="0 0 24 24" aria-hidden="true">
        <circle cx="12" cy="12" r="9.5"/>
        <ellipse cx="12" cy="12" rx="4" ry="9.5"/>
        <path d="M2.5 12h19M4.2 7h15.6M4.2 17h15.6"/>
      </svg>
      <div class="contact-text contact-text--small">marlene@brightcounselpath.net</div>
    </div>
    <div class="rule"></div>

    <div class="contact-item">
      <svg class="contact-icon contact-icon--line" viewBox="0 0 24 24" aria-hidden="true">
        <circle cx="12" cy="8.5" r="4"/>
        <path d="M4 21c0-4.4 3.6-7 8-7s8 2.6 8 7"/>
      </svg>
      <div class="contact-text">@brightcounselpath</div>
    </div>
  </section>

  <section class="card card--back">
    <svg class="bands" viewBox="0 0 360 600" aria-hidden="true">
      <polygon class="band" points="100,0 120,0 0,198 0,165"/>
      <polygon class="band" points="150,0 190,0 0,313 0,247"/>
      <polygon class="band" points="170,600 210,600 360,353 360,287"/>
      <polygon class="band" points="240,600 260,600 360,435 360,402"/>
    </svg>
    <div class="brand-name">Bright Counsel Path</div>
  </section>

</body>
</html>
```